I own a small business whose primary function is Professional Fashion and Commercial Photography and has a secondary function of Talent Management of Models/Actors. I've used PrintaNova in the past to print my own design, but I'd like something a bit more topical, fresh and done by an artist instead of a photographer (me).

My company logo is included with a few selected horizontal (landscape) photos of some of my models--I'd like to use a single model photo as the background for the entire card, either in color or converted to black and white, at opacity enough to see the photo but not too much to obscure any text or the company logo, or use a photo as a share of the card (not the entire background), or use all the three models on the card in some manor... Our company colors are white, black, grey-silver and red.

Industry/Entity Type

Small Business

Contact Information for Business Card

Darnell Voskuijl, Owner
KLT Studios
PO Box 7316
Millbrook VT 05999-7316
(555) 014-2273
dan@kltstudios-example,.com

```html
<!DOCTYPE html>
<html lang="en">
<head>
<meta charset="utf-8">
<title>KLT Studios — Business Card</title>
<link rel="stylesheet" href="https://fonts.googleapis.com/css2?family=Open+Sans:wght@400;600;700&display=swap">
<style>
  :root {
    --page-bg: #e9e7ea;
    --card-white: #ffffff;
    --brand-red: #e82028;
    --ink: #1b1b1b;
    --silver: #8f8a85;
    --rule-grey: #9a9a9a;
    --photo-dark: #3a3a3a;
    --photo-mid: #8a8a8a;
    --photo-light: #c4c4c4;
  }
  * { margin: 0; padding: 0; box-sizing: border-box; }
  html, body {
    width: 1200px; height: 1000px; overflow: hidden;
    background: var(--page-bg);
    font-family: "Open Sans", Arial, sans-serif;
  }
  .card {
    position: absolute; left: 265px; width: 665px; height: 397px;
    border-radius: 22px; overflow: hidden;
    box-shadow: 0 6px 16px rgba(0,0,0,0.25);
  }
  .card--front { top: 73px; background: var(--card-white); }
  .card--back { top: 532px; background: var(--brand-red); }

  .wordmark {
    position: absolute; display: flex; align-items: center; gap: 14px;
    font-weight: 700; letter-spacing: 1px; white-space: nowrap;
  }
  .wordmark__square { display: block; flex: none; }
  .card--front .wordmark { left: 50px; top: 112px; font-size: 56px; color: var(--ink); }
  .card--front .wordmark__square { width: 44px; height: 44px; background: var(--brand-red); }
  .card--back .wordmark { left: 150px; top: 262px; font-size: 40px; color: var(--card-white); }
  .card--back .wordmark__square { width: 32px; height: 32px; border: 3px solid var(--card-white); }

  .contact-name {
    position: absolute; right: 75px; top: 222px;
    font-size: 18px; font-weight: 600; color: var(--ink);
  }
  .contact-name__sep { margin: 0 6px; }
  .contact-lines {
    position: absolute; right: 75px; top: 265px;
    list-style: none; text-align: right;
    font-size: 15.5px; line-height: 23.5px; color: var(--ink);
  }

  .photo-strip {
    position: absolute; left: 0; top: 86px; width: 665px; height: 140px;
    display: flex; background: var(--photo-mid);
  }
  .photo-strip__frame { height: 100%; }
  .photo-strip__frame--1 { width: 168px; background: linear-gradient(135deg, var(--photo-light), var(--photo-dark)); }
  .photo-strip__frame--2 { width: 163px; background: linear-gradient(135deg, var(--photo-dark), var(--photo-light)); }
  .photo-strip__frame--3 { width: 166px; background: linear-gradient(160deg, var(--photo-light), var(--photo-mid)); }
  .photo-strip__frame--4 { width: 168px; background: linear-gradient(120deg, var(--photo-mid), var(--photo-dark)); }
  .photo-strip__dividers { position: absolute; left: 0; top: 72px; }
</style>
</head>
<body>
  <section class="card card--front">
    <div class="wordmark"><span class="wordmark__square"></span>KLT Studios</div>
    <p class="contact-name">Darnell Voskuijl<span class="contact-name__sep">|</span>Owner</p>
    <ul class="contact-lines">
      <li>(555) 014-2273</li>
      <li>dan@kltstudios-example.com</li>
      <li>PO Box 7316 Millbrook VT</li>
    </ul>
  </section>

  <section class="card card--back">
    <div class="photo-strip">
      <div class="photo-strip__frame photo-strip__frame--1" role="img" aria-label="Black and white portrait of a model in a cap"></div>
      <div class="photo-strip__frame photo-strip__frame--2" role="img" aria-label="Black and white portrait of a model in a plaid shirt"></div>
      <div class="photo-strip__frame photo-strip__frame--3" role="img" aria-label="Black and white portrait of a young model outdoors"></div>
      <div class="photo-strip__frame photo-strip__frame--4" role="img" aria-label="Black and white studio portrait of a model"></div>
    </div>
    <svg class="photo-strip__dividers" width="665" height="170" viewBox="0 0 665 170" aria-hidden="true">
      <g stroke="var(--rule-grey)" stroke-width="1.5">
        <line x1="168" y1="0" x2="168" y2="170"/>
        <line x1="331" y1="0" x2="331" y2="170"/>
        <line x1="497" y1="0" x2="497" y2="170"/>
      </g>
    </svg>
    <div class="wordmark"><span class="wordmark__square"></span>KLT Studios</div>
  </section>
</body>
</html>
```